Chimney Service company needs new business card design

We need a updated business card with our new logo added. We provide a full range of chimney services throughout Vermont and New Hampshire. The business card will be one sided and color. Attached is our current business card another document showing all the information we would like on the card.
We dont like a lot of flashy colors.... here is a link to our website to get an idea of our branding www.flueguardianvt.example

Target Market(s)

homeowners

Industry/Entity Type

Business

Contact Information for Business Card

See attached sheet for content.

Font styles to use
Serif
Sans Serif

Requirements
Must have
• all information provided on separate sheet
Should not have
• Additional information that may clogg up design

```html
<!DOCTYPE html>
<html lang="en">
<head>
<meta charset="utf-8">
<title>Flue Guardian – Business Card</title>
<link rel="stylesheet" href="https://fonts.googleapis.com/css2?family=Cinzel:wght@400;600;700&display=swap">
<style>
  :root {
    --page-bg: #e9e7e4;
    --card-white: #ffffff;
    --brand-red: #a30008;
    --band-dark: #333333;
    --ink: #2b2b2b;
    --ink-soft: #444444;
    --on-dark: #ffffff;
  }
  * { box-sizing: border-box; margin: 0; padding: 0; }
  html, body { width: 1200px; height: 1000px; overflow: hidden; }
  body {
    background: var(--page-bg);
    font-family: "Cinzel", Georgia, serif;
    position: relative;
  }
  .business-card {
    position: absolute;
    left: 100px; top: 214px;
    width: 1000px; height: 572px;
    border-radius: 30px;
    overflow: hidden;
    background: var(--card-white);
    box-shadow: 0 10px 30px rgba(0,0,0,.18);
  }
  .identity {
    position: absolute;
    left: 50px; top: 46px;
    width: 400px;
    display: flex;
    flex-direction: column;
    align-items: center;
  }
  .identity-mark {
    width: 84px; height: 84px;
    background: var(--ink);
    margin-bottom: 16px;
  }
  .company-name {
    font-size: 40px;
    font-weight: 600;
    color: var(--ink);
    letter-spacing: 1px;
    line-height: 1;
    white-space: nowrap;
  }
  .company-rule {
    margin-top: 16px;
    width: 100%;
    height: 2px;
    background: var(--ink);
    position: relative;
  }
  .company-est {
    position: absolute;
    left: 50%; top: -10px;
    transform: translateX(-50%);
    padding: 0 10px;
    background: var(--card-white);
    font-size: 15px;
    color: var(--ink);
    letter-spacing: 1px;
    white-space: nowrap;
  }
  .company-region {
    margin-top: 18px;
    font-size: 14px;
    color: var(--ink-soft);
    letter-spacing: .5px;
    white-space: nowrap;
  }
  .services-divider {
    position: absolute;
    left: 478px; top: 40px;
    width: 2px; height: 222px;
    background: var(--brand-red);
  }
  .services {
    position: absolute;
    left: 510px; top: 48px;
  }
  .services-title {
    font-size: 26px;
    font-weight: 600;
    color: var(--brand-red);
    letter-spacing: .5px;
    margin-bottom: 10px;
  }
  .services-list { list-style: none; }
  .services-list li {
    font-size: 19px;
    color: var(--ink);
    line-height: 1.5;
    display: flex;
    align-items: center;
    gap: 10px;
    white-space: nowrap;
  }
  .services-list li::before {
    content: "";
    width: 9px; height: 9px;
    border-radius: 50%;
    background: var(--brand-red);
    flex: none;
  }
  .promise-band {
    position: absolute;
    left: 0; top: 296px;
    width: 100%; height: 54px;
    background: var(--band-dark);
    color: var(--on-dark);
    display: flex; align-items: center; justify-content: center;
    gap: 22px;
    font-size: 25px;
    letter-spacing: .5px;
    border-bottom: 4px solid var(--card-white);
    white-space: nowrap;
  }
  .promise-dot {
    width: 12px; height: 12px; border-radius: 50%;
    background: var(--on-dark);
  }
  .contact-panel {
    position: absolute;
    left: 0; top: 350px;
    width: 100%; height: 222px;
    background: var(--brand-red);
    display: flex;
    justify-content: space-around;
    align-items: center;
    padding: 0 30px;
  }
  .contact-item {
    display: flex; flex-direction: column; align-items: center; gap: 14px;
    color: var(--on-dark);
    font-size: 20px;
    letter-spacing: .5px;
    white-space: nowrap;
  }
  .contact-icon { width: 40px; height: 40px; }
</style>
</head>
<body>
  <main class="business-card">
    <section class="identity">
      <div class="identity-mark"></div>
      <div class="company-name">Flue Guardian</div>
      <div class="company-rule"><span class="company-est">Inc 1989</span></div>
      <p class="company-region">Serving VT and New Hampshire since 1989</p>
    </section>

    <div class="services-divider"></div>
    <section class="services">
      <h2 class="services-title">Services We Provide</h2>
      <ul class="services-list">
        <li>Full Masonry Services</li>
        <li>Historic chimney restoration</li>
        <li>Stainless steel liners</li>
        <li>New Chimney Installations</li>
        <li>Hearthline Certified Chimney sweeps</li>
      </ul>
    </section>

    <div class="promise-band">
      <span>Fully Insured – Free Estimates</span>
      <span class="promise-dot"></span>
      <span>Family owned and operated</span>
    </div>

    <section class="contact-panel">
      <div class="contact-item">
        <svg class="contact-icon" viewBox="0 0 40 40" aria-hidden="true">
          <path d="M9 12c0-2 2-4 4-4l3 5-2 3c1 3 4 6 7 7l3-2 5 3c0 2-2 4-4 4C16 28 9 21 9 12z" fill="#fff"/>
          <path d="M24 8a9 9 0 0 1 8 8M24 13a4 4 0 0 1 3 3" stroke="#fff" stroke-width="2" fill="none" stroke-linecap="round"/>
        </svg>
        <span>802-555-0147</span>
      </div>
      <div class="contact-item">
        <svg class="contact-icon" viewBox="0 0 40 40" aria-hidden="true">
          <rect x="5" y="11" width="30" height="21" fill="#fff"/>
          <path d="M5 11l15 12 15-12" stroke="#a30008" stroke-width="2" fill="none"/>
        </svg>
        <span>info@flueguardianvt.example</span>
      </div>
      <div class="contact-item">
        <svg class="contact-icon" viewBox="0 0 40 40" aria-hidden="true">
          <g stroke="#fff" stroke-width="2" fill="none">
            <circle cx="20" cy="20" r="15"/>
            <ellipse cx="20" cy="20" rx="7" ry="15"/>
            <line x1="5" y1="20" x2="35" y2="20"/>
            <path d="M8 12h24M8 28h24"/>
          </g>
        </svg>
        <span>www.flueguardianvt.example</span>
      </div>
    </section>
  </main>
</body>
</html>
```